RV Wrecking business cards v.2 first was me

So the ones in the picture are my original cards that I came up with. 😅however I kinda messed up on two things, I missed spelled my name it should be Dariel Montoya as well as the email should be Darielm@brightlanecrews.com. I would like to clean this card up and also make it pop! Something that people would remember me by and that screams DEMOLITION. As well as a card that give you a feeling of loyalty and trust. I would also like to change and remove junk hauling and add full demolition to replace it. These cards worked for a little while but I cant make that my image while handing these out. I would also like to only put down that we are located in Cedar Hollow Springs, CA, 95531 instead of the address on the card. Also if we can have a line that states Licensed, Bonded, & Insured. With out License # 4837215

Target Market(s)

Contractors and Home owners

Industry/Entity Type

Construction specialist in Demolition

Contact Information for Business Card

R Wrecking Selective Demolition & Full Demolition Kitchens AD Preparation Bathrooms Sheds Interiors & Exteriors Demo Digging And Much More Darielll Montoya Owner our city state and zip

Font styles to use
Serif
Sans Serif
Decorative

Colors
0054AA
0677BA
7BADD7
CADEEF
E8F1F8
0094D4
00A9DD
6FCCEA
C7EBF8
E9F6FB

Requirements
Must have
• License# 4837215
Nice to have
• Trying to go with a blue and white color scheme
Should not have
• Building construction

```html
<!DOCTYPE html>
<html lang="en">
<head>
<meta charset="utf-8">
<title>RV Wrecking – Business Cards</title>
<link href="https://fonts.googleapis.com/css2?family=Lato:wght@400;700;900&display=swap" rel="stylesheet">
<style>
  :root{
    --bg:#2e2f31;
    --card:#ffffff;
    --ink:#111111;
    --blue:#0f4fa3;
    --blue-dark:#0054aa;
    --rule:#0f4fa3;
  }
  *{box-sizing:border-box;margin:0;padding:0}
  html,body{width:1200px;height:875px;overflow:hidden;background:var(--bg)}
  body{font-family:'Lato',sans-serif;position:relative}
  .card{position:absolute;width:520px;height:298px;background:var(--card);border-radius:16px;overflow:hidden;box-shadow:0 18px 40px rgba(0,0,0,.45)}
  .card--front{left:45px;top:150px}
  .card--back{left:635px;top:420px}

  /* front */
  .front-brand{position:absolute;left:0;right:0;top:92px;display:flex;align-items:center;justify-content:center;gap:14px}
  .brand-dot{width:34px;height:34px;border-radius:50%;background:var(--blue)}
  .front-name{font-weight:900;font-size:56px;color:var(--blue);letter-spacing:1px;text-transform:uppercase}
  .front-license{position:absolute;left:0;right:0;top:172px;display:flex;align-items:center;justify-content:center;gap:10px;font-weight:900;font-size:19px;color:var(--ink);letter-spacing:1px}
  .front-license .rule{width:110px;height:2px;background:var(--rule)}

  /* back */
  .back-title{position:absolute;left:26px;top:22px;font-weight:900;font-size:34px;color:var(--ink);line-height:1}
  .back-sub{position:absolute;left:27px;top:60px;font-weight:900;font-size:10.5px;color:var(--ink);letter-spacing:.3px}
  .services{position:absolute;left:30px;top:80px;list-style:none;font-size:11.5px;color:var(--ink);line-height:1.5;text-transform:uppercase}
  .services li::before{content:"•";margin-right:7px}
  .back-brand{position:absolute;right:26px;top:26px;display:flex;align-items:center;gap:8px}
  .back-brand .brand-dot{width:16px;height:16px}
  .back-brand span{font-weight:900;font-size:24px;color:var(--blue);text-transform:uppercase}
  .divider{position:absolute;left:26px;right:22px;top:158px;height:1.5px;background:var(--rule)}
  .location{position:absolute;right:26px;top:74px;text-align:right;font-size:12px;color:var(--blue);line-height:1.4}
  .person{position:absolute;left:28px;top:172px}
  .person-name{font-weight:900;font-size:26px;color:var(--blue);text-transform:uppercase;letter-spacing:.3px}
  .person-role{font-size:14px;color:var(--blue)}
  .contact{position:absolute;left:28px;top:236px;font-size:13px;color:var(--blue);line-height:1.55}
  .contact-row{display:flex;align-items:center;gap:7px}
  .contact-row svg{width:12px;height:12px;fill:var(--blue)}
  .contact .phone{font-weight:700;font-size:15px}
  .badge{position:absolute;right:0;bottom:0;width:250px;height:40px;background:var(--blue-dark);clip-path:polygon(14px 0,100% 0,100% 100%,0 100%);display:flex;align-items:center;justify-content:center;color:#fff;font-weight:900;font-size:12.5px;letter-spacing:.4px}
</style>
</head>
<body>
  <section class="card card--front">
    <div class="front-brand">
      <div class="brand-dot"></div>
      <div class="front-name">RV Wrecking</div>
    </div>
    <div class="front-license"><span class="rule"></span>LICENSE# 4837215</div>
  </section>

  <section class="card card--back">
    <h1 class="back-title">R WRECKING</h1>
    <p class="back-sub">SELECTIVE DEMOLITION &amp; FULL DEMOLITION</p>
    <ul class="services">
      <li>Kitchens • ADU Preparation</li>
      <li>Bathrooms • Sheds</li>
      <li>Interiors &amp; Exteriors Demo</li>
      <li>Digging &amp; Much More</li>
    </ul>
    <div class="back-brand"><div class="brand-dot"></div><span>RV Wrecking</span></div>
    <div class="location">Cedar Hollow<br>Springs, CA, 95531</div>
    <div class="divider"></div>
    <div class="person">
      <div class="person-name">Dariel Montoya</div>
      <div class="person-role">Owner</div>
    </div>
    <div class="contact">
      <div class="contact-row phone"><svg viewBox="0 0 24 24"><path d="M6.6 10.8a15.1 15.1 0 0 0 6.6 6.6l2.2-2.2a1 1 0 0 1 1-.25 11.4 11.4 0 0 0 3.6.57 1 1 0 0 1 1 1V20a1 1 0 0 1-1 1A17 17 0 0 1 3 4a1 1 0 0 1 1-1h3.5a1 1 0 0 1 1 1c0 1.25.2 2.45.57 3.57a1 1 0 0 1-.25 1z"/></svg>(555)204-7318</div>
      <div class="contact-row"><svg viewBox="0 0 24 24"><path d="M2 5h20v14H2zm2 2v.5l8 5 8-5V7zm0 2.8V17h16V9.8l-8 5z"/></svg>Darielm@brightlanecrews.com</div>
    </div>
    <div class="badge">LICENSED, BONDED, &amp; INSURED</div>
  </section>
</body>
</html>
```